Dental Magazine Cover

I need a template created for a magazine cover. Magazine title is "Dentistry Halvern"

I would like to have a logo designed for "Dentistry Halvern"

For each issue, we would like to keep the same basic template and change out the photos, text, etc. according to the contents of the issue.

You can create the cover of the first issue with the attached photos and captions:

Date for use on magazine cover is February 2014

Main caption: Maxillary Reconstruction with Immediately Loaded Dental Implants
(Use attached File 1 for main photo. Photo may be cropped and rotated as needed)

Inset: Bisphosphonate Guidelines for Dental Treatment
(Use attached file 2 for inset photo. Photo may be cropped and rotated as needed).

Target Market(s)

Target audience for this magazine are dentists, dental hygienists, dental assistants, and dental professionals in the Austin, Texas area.

Industry/Entity Type

Dental

Other font styles liked:
• Font need to "POP"

Requirements
Must have
• Please see project overview guidelines. Magazine cover needs to have the following:
1) Logo
2) Main image
3) Caption for Main image (Maxillary Reconstruction with Immediately Loaded Dental Implants)
4) Smaller Inset Photo
5) Caption for smaller inset photo (Bisphosphonate Guidelines for Dental Treatment)
6) Date of magazine issue (February 2014)

Use any of the Photos you see fit to make the magazine cover work.
Nice to have
• Please try to make the "Dentistry Halvern" logo "POP". Dental journals are boring enough. We can at least have a logo that pops. Simply using generic text will win this design. The below text is just a suggestion of a Logo. Please feel free to use all creative license in making a logo that has some sizzle. PLEASE NOTE: A tooth is NOT needed in the logo...

```html
<!DOCTYPE html>
<html lang="en">
<head>
<meta charset="utf-8">
<title>Dentistry Halvern – February 2014</title>
<link rel="stylesheet" href="https://fonts.googleapis.com/css2?family=Anton&family=Oswald:wght@700&family=Josefin+Sans:wght@200;300&display=swap">
<style>
  :root {
    --cyan: #4dd3f6;
    --ink: #111111;
    --paper: #ffffff;
    --band: #000000;
    --date-bg: #e6e6e6;
    --photo-dark: #0b0b0b;
    --photo-warm: #8a4a3a;
    --photo-light: #e8e2d6;
  }
  * { margin: 0; padding: 0; box-sizing: border-box; }
  html, body { width: 934px; height: 1200px; overflow: hidden; background: var(--paper); }
  .cover { position: relative; width: 934px; height: 1200px; background: var(--paper); overflow: hidden; }

  .masthead { position: absolute; left: 0; top: 0; width: 934px; height: 330px; }
  .masthead text { font-family: "Anton", "Oswald", sans-serif; fill: var(--cyan); }

  .issue-date {
    position: absolute; left: 535px; top: 227px; width: 399px; height: 93px;
    background: var(--date-bg);
    display: flex; align-items: center; justify-content: center;
    font-family: "Josefin Sans", sans-serif; font-weight: 300;
    font-size: 44px; color: var(--cyan); letter-spacing: 1px;
  }

  .feature-band { position: absolute; left: 0; top: 360px; width: 934px; height: 148px; background: var(--band); }
  .feature-title { position: absolute; left: 0; top: 0; width: 420px; height: 148px; }
  .feature-title text { font-family: "Oswald", sans-serif; font-weight: 700; fill: var(--cyan); }
  .feature-subtitle {
    position: absolute; left: 428px; top: 12px;
    font-family: "Josefin Sans", sans-serif; font-weight: 200;
    font-size: 36px; line-height: 43px; letter-spacing: 1.5px;
    color: var(--paper); text-transform: uppercase;
  }

  .main-photo {
    position: absolute; left: 0; top: 508px; width: 934px; height: 377px;
    background:
      radial-gradient(ellipse 48% 32% at 50% 72%, var(--photo-light) 0%, rgba(232,226,214,0.6) 45%, transparent 75%),
      radial-gradient(ellipse 52% 26% at 50% 40%, var(--photo-warm) 0%, rgba(138,74,58,0.4) 55%, transparent 80%),
      radial-gradient(ellipse 55% 20% at 50% 10%, #d9b38a 0%, transparent 75%),
      var(--photo-dark);
  }

  .inset-photo {
    position: absolute; left: 0; top: 900px; width: 280px; height: 280px;
    background:
      radial-gradient(circle at 25% 30%, #3fd07a 0%, transparent 45%),
      radial-gradient(circle at 70% 25%, #e24a8a 0%, transparent 45%),
      radial-gradient(circle at 40% 75%, #4a6de0 0%, transparent 50%),
      radial-gradient(circle at 80% 80%, #e6c84a 0%, transparent 45%),
      #1a1024;
  }

  .inset-caption {
    position: absolute; left: 293px; top: 985px;
    font-family: "Josefin Sans", sans-serif; font-weight: 200; color: var(--cyan);
  }
  .inset-caption .headline { display: block; font-size: 41px; line-height: 48px; letter-spacing: 0.5px; text-transform: uppercase; }
  .inset-caption .kicker { display: block; font-size: 38px; line-height: 50px; font-weight: 300; }
</style>
</head>
<body>
  <main class="cover">
    <svg class="masthead" viewBox="0 0 934 330" aria-label="Dentistry Halvern">
      <text x="60" y="205" font-size="212" textLength="820" lengthAdjust="spacingAndGlyphs">DENTISTRY</text>
      <text x="55" y="318" font-size="124" textLength="462" lengthAdjust="spacingAndGlyphs">HALVERN</text>
    </svg>

    <div class="issue-date">February 2014</div>

    <section class="feature-band">
      <svg class="feature-title" viewBox="0 0 420 148" aria-label="Maxillary Reconstruction">
        <text x="50" y="72" font-size="70" textLength="333" lengthAdjust="spacingAndGlyphs">MAXILLARY</text>
        <text x="50" y="131" font-size="46" textLength="333" lengthAdjust="spacingAndGlyphs">RECONSTRUCTION</text>
      </svg>
      <p class="feature-subtitle">With immediately<br>loaded dental<br>implants</p>
    </section>

    <div class="main-photo" role="img" aria-label="Photo of a full upper implant-supported denture on a stone model with abutments, on a black background"></div>

    <div class="inset-photo" role="img" aria-label="Colourful micro-scan image of trabecular bone structure"></div>

    <p class="inset-caption">
      <span class="headline">Bisphosphonate Guidelines</span>
      <span class="kicker">for Dental Treatment</span>
    </p>
  </main>
</body>
</html>
```